Business Card Design for Photographer

Updating business card design. Must use included logo. We're a luxury wedding photography business. Elegancy, luxury, consistency are messages we wish to convey.

Visit our website at www.colbyvarnway.com to familiarize yourself more with our brand design currently (fonts, colors etc.). This is what we want to maintain.

Target Market(s)

Luxury Brides and Grooms

Industry/Entity Type

Wedding

Contact Information for Business Card

Current logo (attached to brief)
Name: Colby Varnway
Phone: 5208813047
website/blog
Email

Requirements
Must have
• Current logo (attached to brief)
• Name: Colby Varnway
• Phone: 5208813047
• website/blog
• Email
• Instagram username
Should not have
• bright colors, fonts that don't suit our brand (visit www.colbyvarnway.com)

```html
<!DOCTYPE html>
<html lang="en">
<head>
<meta charset="utf-8">
<title>Colby Varnway Photographers — Business Card</title>
<link rel="stylesheet" href="https://fonts.googleapis.com/css2?family=Cinzel:wght@400&family=Cormorant+Garamond:ital,wght@1,400&family=Jost:wght@400&display=swap">
<style>
  :root {
    --backdrop: #e9e7e4;
    --card-grey: #7c7c7c;
    --card-white: #fbfbfa;
    --ink-white: #ffffff;
    --ink-grey: #6f6f6f;
    --shadow: rgba(0, 0, 0, 0.18);
  }
  * { margin: 0; padding: 0; box-sizing: border-box; }
  html, body {
    width: 1200px; height: 800px; overflow: hidden;
    background: var(--backdrop);
  }
  .stage {
    width: 1200px; height: 800px;
    display: flex; align-items: center; justify-content: center; gap: 60px;
  }
  .card {
    position: relative;
    width: 500px; height: 286px;
    box-shadow: 0 6px 18px var(--shadow);
    overflow: hidden;
  }

  /* Front */
  .card--front { background: var(--card-grey); color: var(--ink-white); }
  .brand {
    position: absolute; left: 0; right: 0; top: 96px;
    display: flex; flex-direction: column; align-items: center;
  }
  .brand__mark {
    width: 26px; height: 26px; background: var(--ink-white); margin-bottom: 16px;
  }
  .brand__name {
    font-family: "Cinzel", serif; font-size: 24px; letter-spacing: 0.22em;
  }
  .brand__tag {
    margin-top: 6px;
    font-family: "Cinzel", serif; font-size: 11px; letter-spacing: 0.55em;
  }
  .front__web {
    position: absolute; right: 26px; bottom: 22px;
    font-family: "Cormorant Garamond", serif; font-style: italic;
    font-size: 17px; letter-spacing: 0.04em;
  }

  /* Back */
  .card--back { background: var(--card-white); color: var(--ink-grey); }
  .back__panel {
    position: absolute; right: 0; top: 0;
    width: 290px; height: 170px; background: var(--card-grey);
  }
  .back__name {
    position: absolute; left: 28px; top: 186px;
    font-family: "Cormorant Garamond", serif; font-style: italic;
    font-size: 19px; letter-spacing: 0.32em;
  }
  .contact {
    position: absolute; left: 28px; bottom: 20px;
    list-style: none;
    font-family: "Jost", sans-serif; font-size: 13px; letter-spacing: 0.06em;
  }
  .contact__item { display: flex; align-items: center; gap: 8px; line-height: 20px; }
  .contact__icon { width: 11px; height: 11px; flex: none; fill: var(--ink-grey); }
</style>
</head>
<body>
<main class="stage">
  <section class="card card--front" aria-label="Business card front">
    <div class="brand">
      <span class="brand__mark"></span>
      <span class="brand__name">Colby Varnway</span>
      <span class="brand__tag">PHOTOGRAPHERS</span>
    </div>
    <p class="front__web">colbyvarnway.com</p>
  </section>

  <section class="card card--back" aria-label="Business card back">
    <div class="back__panel"></div>
    <p class="back__name">colby varnway</p>
    <ul class="contact">
      <li class="contact__item">
        <svg class="contact__icon" viewBox="0 0 12 12" aria-hidden="true"><path d="M2.5 1 L4.5 1 L5.3 3.4 L4 4.4 Q5 6.8 7.6 8 L8.6 6.7 L11 7.5 L11 9.5 Q10.5 11 9 11 Q1 10 1 3 Q1 1.5 2.5 1 Z"/></svg>
        (520) 881-3047
      </li>
      <li class="contact__item">
        <svg class="contact__icon" viewBox="0 0 12 12" aria-hidden="true"><rect x="0" y="2" width="12" height="8"/><path d="M0.5 2.5 L6 6.5 L11.5 2.5" stroke="#fbfbfa" stroke-width="1" fill="none"/></svg>
        colby@colbyvarnway.com
      </li>
      <li class="contact__item">
        <svg class="contact__icon" viewBox="0 0 12 12" aria-hidden="true"><rect x="0.5" y="0.5" width="11" height="11"/></svg>
        colbyvarnwayphoto
      </li>
    </ul>
  </section>
</main>
</body>
</html>
```